BrightHarbor Web Design Project

BrightHarbor IT solutions, a IT mananaged services company is looking to redesign current website (brightharborsolutions.example).

The website should convey professionalism within the managed it services community. The layout should invite users to explore other areas of the site. Should contain tools and other current information that clients or potential clients would find useful. Product pages, special offers and informational pages should be easily editable by non-programmers. Tidewardnet.example is a good site to review as an example of the design components we like.

Target Market(s)

Professional services companies with 10-100 users

Industry/Entity Type

It Company

Requirements
Must have
• • Clickable icons and graphics are good
• SEO - Wordpress could be a great platform for us to work from as we already have internal experience with it and it’s easy to update. If not Wordpress, we would need something that is easy to SEO optimize
• An “our team” section with pictures
• Sell the message to potential clients why they need managed services
• Home page needs to convey our core services at a glance
• Home page needs to load quickly
• Screenshots of our monitoring and security reports
• Easy for us to update/edit certain areas
o New products
o Testimonials
Nice to have
• • Something like TN’s savings calculator - http://www.tidewardnet.example/it-savings-calculator/
• Webform to enter service ticket requests
• Motion of home page banner
• Maybe pull in RSS feeds from current tech news sources
• Rotating content on all pages to keep it fresh
• “Harbor-up” feature for monthly promos
Should not have
• • Should not be overly "techie" in feel.
• Not overly wordy (like current site)

```html
<!DOCTYPE html>
<html lang="en">
<head>
<meta charset="utf-8">
<title>BrightHarbor IT Solutions</title>
<link rel="stylesheet" href="https://fonts.googleapis.com/css2?family=Ubuntu:wght@300;400;500;700&family=PT+Serif&display=swap">
<style>
:root{
  --green:#8cc152;
  --green-soft:#a9d47a;
  --green-dark:#4f9a2a;
  --green-pill:#6cae3c;
  --blue:#1a73c0;
  --ink:#2b2b2b;
  --text:#555;
  --grey-panel:#efefef;
  --grey-line:#d7d7d7;
  --grey-num:#d3d3d3;
  --footer:#5f5f5f;
  --testi-bg:#e9f5d9;
}
*{box-sizing:border-box;margin:0;padding:0}
html,body{width:1200px;height:1042px;overflow:hidden;background:#fff}
body{font-family:"Ubuntu",sans-serif;color:var(--ink);position:relative}
.abs{position:absolute}
a{color:inherit;text-decoration:none}

/* header */
.site-header{left:0;top:0;width:1200px;height:117px}
.header-decor{left:0;top:0;width:1200px;height:117px;
  background:linear-gradient(90deg,#b7dc86 0%,#f4f8ee 18%,#fff 40%,#fff 70%,#eef6e2 85%,#b9dd8a 100%)}
.brand{left:212px;top:28px;width:112px;text-align:center}
.brand-mark{display:inline-block;width:34px;height:34px;border-radius:50%;background:var(--green)}
.brand-name{display:block;font-size:16px;font-weight:500;color:var(--green-dark);margin-top:4px}
.brand-sub{display:block;font-size:8px;font-weight:700;letter-spacing:1px;color:#333}
.header-divider{left:335px;top:13px;width:1px;height:100px;background:#ddd}
.account-links{right:188px;top:25px;font-size:11px;color:#222}
.search{left:831px;top:57px;width:181px;height:20px;border:1px solid #555;background:#fff}
.search span{position:absolute;left:5px;top:3px;font-size:9px;font-style:italic;color:#333}
.search-btn{position:absolute;right:-1px;top:-1px;width:24px;height:20px;background:#3a3a3a}
.main-nav{left:357px;top:91px;display:flex;gap:0;font-size:11.5px;color:#444}
.main-nav li{list-style:none;margin-right:18px;white-space:nowrap}
.main-nav li.active{color:#111}
.main-nav li::after{content:"▼";font-size:8px;margin-left:4px;color:#555}
.main-nav li.active::after{color:var(--green-dark)}
.careers{left:957px;top:92px;width:57px;height:14px;border-radius:8px;background:var(--green-pill);color:#fff;font-size:9px;text-align:center;line-height:14px}

/* hero */
.hero-band{left:0;top:117px;width:1200px;height:323px;background:var(--green)}
.hero-panel{left:187px;top:117px;width:836px;height:323px;background:var(--grey-panel)}
.hero-art{left:248px;top:140px;width:340px;height:280px;border-radius:40% 40% 30% 30%;
  background:radial-gradient(ellipse at 45% 40%,#8bc862 0%,#4f9a2a 35%,rgba(220,230,215,.6) 65%,rgba(239,239,239,0) 80%)}
.hero-num{left:803px;top:140px;font-family:"PT Serif",serif;font-size:178px;line-height:1;color:var(--grey-num);letter-spacing:-6px}
.hero-kicker{left:865px;top:221px;font-family:"PT Serif",serif;font-size:16px;color:#555}
.hero-kicker::before{content:"";position:absolute;left:-14px;top:5px;width:10px;height:10px;background:var(--green)}
.hero-copy{left:621px;top:306px;width:340px;font-size:14px;font-weight:300;line-height:18px;color:#444}
.hero-more{left:884px;top:329px;font-size:9.5px;color:var(--green-dark)}
.hero-ring{left:938px;top:327px;width:16px;height:16px;border-radius:50%;border:3px solid var(--green-pill)}
.feature-tab{top:354px;height:23px;border-top:1px solid #bbb;border-bottom:1px solid #bbb;font-size:10px;color:#444;display:flex;align-items:center;padding-left:6px;gap:6px}
.hero-progress{left:340px;top:435px;width:535px;height:7px;display:flex;gap:2px}
.hero-progress span{flex:1;background:#d5d5d5}
.hero-progress span.on{background:#4a4a4a}

/* testimonial */
.testi-label{left:199px;top:448px;width:105px;height:31px;border:4px solid #c9c9c9;border-right:6px solid #555;background:#fff;font-size:10px;color:var(--blue);display:flex;align-items:center;justify-content:center}
.testi-quote{left:306px;top:448px;width:711px;height:31px;background:var(--testi-bg);border-bottom:3px solid #c6e3a4;font-size:9px;color:#333;display:flex;align-items:center;padding-left:17px;white-space:nowrap}
.testi-quote b{margin-left:10px}

/* tabs panel */
.tabs-panel{left:196px;top:501px;width:521px;height:189px;border:1px solid #e2e2e2;background:#f6f6f6}
.tab{top:509px;height:34px;font-size:11px;font-weight:500;color:#222;display:flex;align-items:center;justify-content:center;border:1px solid #cfcfcf;background:linear-gradient(#fafafa,#e4e4e4)}
.tab.active{background:#f2f2f2;border-bottom-color:#f2f2f2}
.tab-body{left:200px;top:543px;width:517px;height:147px;background:#f2f2f2}
.tab-text{left:220px;top:557px;width:310px;font-size:10.4px;font-weight:300;line-height:14px;color:#555}
.tab-divider{left:541px;top:553px;width:1px;height:130px;background:#ddd}
.pill{border-radius:9px;color:#fff;font-size:9px;text-align:center}
.view-more{left:465px;top:657px;width:57px;height:15px;background:#4d4d4d;line-height:15px}
.tab-art{left:590px;top:550px;width:76px;height:136px;border-radius:30px 30px 8px 8px;background:linear-gradient(#b3b3b3,#7d7d7d 60%,rgba(242,242,242,0))}

/* people */
.people-title{left:732px;top:506px;font-size:12px;font-weight:500;color:#222}
.people-strip{left:730px;top:527px;width:285px;height:55px;border:1px solid #ddd;background:#fff}
.person{top:534px;width:36px;height:34px;background:linear-gradient(#c9b6a3,#8d7a6a)}
.people-scroll{left:741px;top:576px;width:261px;height:1px;background:#ccc}
.people-scroll::before{content:"";position:absolute;left:20px;top:-1px;width:10px;height:2px;background:#555}
.people-box{left:730px;top:587px;width:278px;height:103px;border-left:1px solid #ddd;border-top:1px solid #eee}
.people-text{left:737px;top:597px;width:272px;font-size:9.2px;line-height:12px;color:#555}
.people-more{left:949px;top:671px;width:53px;height:15px;background:var(--green-pill);line-height:15px;font-size:8px}

/* news */
.news{left:200px;top:719px;width:813px;height:54px;border:2px solid #eee;background:#fff}
.news-icon{left:215px;top:737px}
.news-title{left:242px;top:741px;font-size:13px;color:var(--blue);font-weight:300}
.news-date{left:380px;top:744px;font-size:9.5px;color:#333}
.news-head{left:466px;top:744px;font-size:9.5px;color:var(--blue)}
.news-list{left:940px;top:744px;font-size:9.5px;color:var(--blue)}
.news-list-btn{left:988px;top:742px;width:13px;height:13px;border-radius:50%;border:1px solid #bbb}

/* promos */
.promo{top:797px;height:55px;border:2px solid #eee;background:#fff}
.calc-art{left:212px;top:787px;width:49px;height:74px;border-radius:6px;background:linear-gradient(#7a7a7a,#555)}
.promo-title{font-size:11px;color:var(--blue);font-weight:500;line-height:14px}
.promo-sub{left:273px;top:829px;font-size:9.3px;color:#333}
.play{left:628px;top:815px;width:20px;height:20px;border-radius:50%;border:1px solid #bbb;background:#f5f5f5}
.video-art{left:902px;top:802px;width:107px;height:44px;background:linear-gradient(90deg,#d9d3cc,#6f6a66 50%,#cfc6bd)}

/* footer */
.site-footer{left:0;top:911px;width:1200px;height:131px;background:var(--footer)}
.footer-brand{left:197px;top:911px;width:78px;height:62px;background:#fff;text-align:center;padding-top:8px}
.footer-brand .brand-mark{width:22px;height:22px;background:#9a9a9a}
.footer-brand .brand-name{font-size:9.5px;color:#666;margin-top:2px;font-weight:400}
.footer-nav{left:296px;top:920px;display:flex;font-size:9.5px;color:#fff}
.footer-nav li{list-style:none;white-space:nowrap}
.footer-nav li+li::before{content:"|";margin:0 20px}
.follow{left:591px;top:958px;font-size:9px;color:#ddd}
.social{width:25px;height:25px;border:1px solid #ccc;background:#6b6b6b}
.footer-divider{left:718px;top:960px;width:1px;height:53px;background:#888}
.footer-links{left:728px;top:958px;font-size:9px;color:#ddd;white-space:nowrap}
.footer-legal{left:728px;top:981px;width:290px;font-size:7.6px;line-height:11px;color:#ddd}
</style>
</head>
<body>

<header class="abs site-header">
  <div class="abs header-decor" role="img" aria-label="Soft green leaves decorating the header edges"></div>
  <div class="abs brand"><span class="brand-mark"></span><span class="brand-name">BrightHarbor</span><span class="brand-sub">IT SOLUTIONS</span></div>
  <div class="abs header-divider"></div>
  <div class="abs account-links">Login | &nbsp;Register | Help</div>
  <div class="abs search"><span>Search |</span>
    <div class="search-btn"><svg width="24" height="20" viewBox="0 0 24 20"><circle cx="11" cy="9" r="5" fill="none" stroke="#fff" stroke-width="2"/><line x1="14.5" y1="12.5" x2="18" y2="16" stroke="#fff" stroke-width="2.4"/></svg></div>
  </div>
  <ul class="abs main-nav">
    <li class="active">Home</li><li>About us</li><li>Solutions</li><li>Contacts</li><li>Data Backup</li><li>Testimonial</li><li>People</li><li>Blog</li>
  </ul>
  <a class="abs careers">Careers</a>
</header>

<section>
  <div class="abs hero-band"></div>
  <div class="abs hero-panel"></div>
  <div class="abs hero-art" role="img" aria-label="Green light bulb with an at sign standing on a patch of grass"></div>
  <div class="abs hero-num">01</div>
  <div class="abs hero-kicker">Wisdom</div>
  <p class="abs hero-copy">We promote continual education for our clients and ourselves.</p>
  <a class="abs hero-more">read more</a>
  <div class="abs hero-ring"></div>
  <div class="abs feature-tab" style="left:615px;width:108px">
    <svg width="11" height="12" viewBox="0 0 11 12"><circle cx="5.5" cy="4.5" r="3.8" fill="none" stroke="#222" stroke-width="1.6"/><rect x="3.5" y="8.5" width="4" height="3" fill="#222"/></svg>Feature One</div>
  <div class="abs feature-tab" style="left:732px;width:106px">
    <svg width="11" height="11" viewBox="0 0 11 11"><circle cx="5.5" cy="5.5" r="4.5" fill="none" stroke="#222" stroke-width="1.8"/></svg>Feature Two</div>
  <div class="abs feature-tab" style="left:849px;width:108px">
    <svg width="11" height="11" viewBox="0 0 11 11"><path d="M5.5 1 L10 5.5 L5.5 10 L1 5.5Z" fill="none" stroke="#222" stroke-width="1.5"/></svg>Feature Three</div>
  <div class="abs hero-progress"><span class="on"></span><span></span><span></span><span></span><span></span></div>
</section>

<section>
  <div class="abs testi-label">TESTIMONIAL</div>
  <div class="abs testi-quote">«Sed ut perspiciatis unde omnis iste natus error sit voluptatem accusantium doloremque laudantium, totam rem aperia», <b>Auae ab illo</b></div>
</section>

<section>
  <div class="abs tabs-panel"></div>
  <div class="abs tab-body"></div>
  <div class="abs tab active" style="left:200px;width:165px">KNOW &nbsp;OUR COMPANY</div>
  <div class="abs tab" style="left:365px;width:176px">COMPLETE IT SOLUTIONS</div>
  <div class="abs tab" style="left:541px;width:176px">WHAT IS NEW?</div>
  <p class="abs tab-text">In the information age of today, one must stay abreast of current technology in order to thrive. New dvancements are made daily in dispersing information and collaborative computing. High-speed networks aid in the exchange of electronic information between businesses, their customers, vendors, and peers. Businesses that are quick to act and effectively implement this technology will rise to the top.</p>
  <a class="abs pill view-more">View More</a>
  <div class="abs tab-divider"></div>
  <div class="abs tab-art" role="img" aria-label="Grey studio microphone"></div>
</section>

<section>
  <h2 class="abs people-title">OUR PEOPLE</h2>
  <div class="abs people-strip"></div>
  <div class="abs person" style="left:738px" role="img" aria-label="Team member portrait"></div>
  <div class="abs person" style="left:777px" role="img" aria-label="Team member portrait"></div>
  <div class="abs person" style="left:817px" role="img" aria-label="Team member portrait"></div>
  <div class="abs person" style="left:856px" role="img" aria-label="Team member portrait"></div>
  <div class="abs person" style="left:895px" role="img" aria-label="Team member portrait"></div>
  <div class="abs person" style="left:934px" role="img" aria-label="Team member portrait"></div>
  <div class="abs person" style="left:973px" role="img" aria-label="Team member portrait"></div>
  <div class="abs people-scroll"></div>
  <div class="abs people-box"></div>
  <p class="abs people-text">Veritatis et quasi architecto beatae vitae dicta sunt explicabo. Nemo enim ipsam voluptatem quia voluptas sit aspernatur aut odit aut fugit, sed quia consequuntur magni dolores eos qui ratione voluptatem sequi .explicabo. Nemo enim ipsam voluptatem quia voluptas sit aspernatur aut odit aut fugit, sed quia consequuntur</p>
  <a class="abs pill people-more">Read more</a>
</section>

<section>
  <div class="abs news"></div>
  <svg class="abs news-icon" width="22" height="22" viewBox="0 0 22 22"><circle cx="11" cy="11" r="10" fill="none" stroke="#6cae3c" stroke-width="1.5"/><line x1="4" y1="8" x2="18" y2="8" stroke="#6cae3c" stroke-width="1.5"/><line x1="3" y1="11" x2="19" y2="11" stroke="#6cae3c" stroke-width="1.5"/><line x1="4" y1="14" x2="18" y2="14" stroke="#6cae3c" stroke-width="1.5"/></svg>
  <h2 class="abs news-title">News Center</h2>
  <span class="abs news-date">Jan 26, 2012</span>
  <a class="abs news-head">Sed ut perspiciatis unde omnis iste natus error sit voluptatem accusantium</a>
  <a class="abs news-list">Show List</a>
  <svg class="abs news-list-btn" viewBox="0 0 13 13"><path d="M3.5 5 L6.5 8 L9.5 5Z" fill="#999"/></svg>
</section>

<section>
  <div class="abs promo" style="left:198px;width:466px"></div>
  <div class="abs calc-art" role="img" aria-label="Grey calculator"></div>
  <h3 class="abs promo-title" style="left:273px;top:812px">WHAT ARE YOUR IT SUPPORT REQUIREMENTS AND COSTS ?</h3>
  <p class="abs promo-sub">Try our IT Resource Calculator and find out what your business needs.</p>
  <svg class="abs play" viewBox="0 0 20 20"><path d="M8 6 L13 10 L8 14Z" fill="#777"/></svg>

  <div class="abs promo" style="left:671px;width:342px"></div>
  <h3 class="abs promo-title" style="left:686px;top:807px">SEE OUR LEATEST VIDEO WITH NEW<br>PRODUCT LOUNCH !</h3>
  <div class="abs video-art" role="img" aria-label="Video still of a product launch presentation"></div>
</section>

<footer class="abs site-footer"></footer>
<div class="abs footer-brand"><span class="brand-mark"></span><span class="brand-name">BrightHarbor</span></div>
<ul class="abs footer-nav"><li>Home</li><li>About us</li><li>Solutions</li><li>Contacts</li><li>Data Backup</li><li>Testimonial</li><li>People</li><li>Blog</li></ul>
<span class="abs follow">follow us on:</span>
<div class="abs social" style="left:657px;top:960px" role="img" aria-label="Social network link"></div>
<div class="abs social" style="left:687px;top:960px" role="img" aria-label="Social network link"></div>
<div class="abs social" style="left:657px;top:988px" role="img" aria-label="Social network link"></div>
<div class="abs social" style="left:687px;top:988px" role="img" aria-label="News feed link"></div>
<div class="abs footer-divider"></div>
<div class="abs footer-links">Terms &amp; Conditions &nbsp;| &nbsp;&nbsp;Privacy &amp; Policy &nbsp;&nbsp;| &nbsp;&nbsp;&nbsp;Help &nbsp;&nbsp;| &nbsp;&nbsp;&nbsp;Search</div>
<p class="abs footer-legal">Tideward: I.T. Support, Information Technology Services, IT Consulting Experts for Small and Medium Businesses Nationwide. Tideward is a division of BrightHarbor IT Solutions</p>

</body>
</html>
```